We want a business card/punch card for our business. We are including examples of our current business card (we like the front of our business card and not looking to remake it). We need only back side to be designed in form of a punch card (we are including a sample of the punch card we made, but are unsatisfied). For each $180 spend (9 punches) our clients have $20 off.

Colors
886aae

```html
<!DOCTYPE html>
<html lang="en">
<head>
<meta charset="utf-8">
<title>Lotus Path – Business Card &amp; Punch Card</title>
<link href="https://fonts.googleapis.com/css2?family=Arimo:wght@400;700&family=Oswald:wght@500;600&family=Kaushan+Script&display=swap" rel="stylesheet">
<style>
  :root {
    --backdrop: #e6e6e8;
    --lavender-light: #dcdff0;
    --lavender-mid: #c4c8e6;
    --violet-deep: #7a3aa0;
    --violet-blue: #7070bb;
    --violet-band: #7c76c0;
    --brand: #886aae;
    --punch-ink: #6a2d92;
    --teal: #1fa39a;
    --ocean: #3f72a0;
    --rose: #d8588f;
    --white: #ffffff;
  }
  * { box-sizing: border-box; margin: 0; padding: 0; }
  html, body { width: 1200px; height: 1132px; overflow: hidden; }
  body { background: var(--backdrop); position: relative; font-family: "Arimo", Arial, sans-serif; }

  .card {
    position: absolute;
    left: 210px;
    width: 780px;
    height: 446px;
    overflow: hidden;
    box-shadow: 0 6px 14px rgba(0,0,0,0.18);
  }
  .card--front { top: 92px; }
  .card--back  { top: 598px; }

  /* Front */
  .front-art { position: absolute; inset: 0; }
  .mandala-field {
    position: absolute; left: 0; top: 0; width: 520px; height: 446px;
    background: radial-gradient(circle at 200px 210px, var(--lavender-light) 0%, var(--lavender-mid) 75%);
  }
  .brand-lockup {
    position: absolute; left: 70px; top: 300px;
    display: flex; align-items: center; gap: 14px;
  }
  .brand-dot { width: 34px; height: 34px; border-radius: 50%; background: var(--brand); }
  .brand-name { font-family: "Arimo", Arial, sans-serif; font-weight: 700; font-size: 52px; color: var(--brand); }

  .contact-name { position: absolute; right: 78px; top: 50px; text-align: right; color: var(--white); }
  .contact-name .person { font-size: 24px; }
  .contact-name .phone { font-size: 24px; margin-top: 2px; }

  .contact-web { position: absolute; right: 60px; top: 220px; text-align: right; color: var(--white); font-size: 19px; line-height: 1.35; }
  .contact-web .gap { margin-top: 22px; }

  /* Back */
  .wash {
    position: absolute; left: 0; top: 0; width: 780px; height: 340px;
    background:
      radial-gradient(ellipse at 20% 85%, var(--teal) 0%, transparent 55%),
      radial-gradient(ellipse at 85% 40%, var(--rose) 0%, transparent 60%),
      linear-gradient(100deg, var(--teal) 0%, var(--ocean) 40%, #8a5ea8 65%, var(--rose) 100%);
  }
  .offer {
    position: absolute; left: 58px; top: 100px;
    font-family: "Oswald", "Arial Narrow", sans-serif; font-weight: 600;
    font-size: 40px; line-height: 52px; letter-spacing: 3px;
    text-transform: uppercase; color: var(--white);
  }
  .offer .highlight { color: var(--punch-ink); }

  .punch-grid {
    position: absolute; left: 470px; top: 60px;
    display: grid; grid-template-columns: repeat(3, 88px); gap: 16px 22px;
  }
  .punch {
    width: 88px; height: 78px; border-radius: 50%;
    background: var(--white); border: 3px solid var(--punch-ink);
    display: flex; align-items: center; justify-content: center;
    font-family: "Oswald", "Arial Narrow", sans-serif; font-weight: 600;
    font-size: 30px; color: var(--punch-ink);
  }

  .services-band {
    position: absolute; left: 0; top: 340px; width: 780px; height: 106px;
    background: var(--violet-band); border-top: 3px solid var(--punch-ink);
  }
  .services {
    position: absolute; left: 60px; top: 14px;
    font-family: "Kaushan Script", cursive; font-size: 24px; line-height: 40px; color: var(--white);
  }
  .band-mark {
    position: absolute; right: 40px; top: 30px;
    display: flex; align-items: center; gap: 8px;
  }
  .band-mark .brand-dot { width: 16px; height: 16px; background: var(--white); }
  .band-mark .brand-name { font-size: 22px; color: var(--white); }
</style>
</head>
<body>

  <section class="card card--front" aria-label="Business card front">
    <svg class="front-art" width="780" height="446" viewBox="0 0 780 446">
      <rect width="780" height="446" fill="var(--lavender-mid)"/>
      <path d="M470 0 C395 120 395 320 465 446 L780 446 L780 0 Z" fill="#a9acda"/>
      <path d="M500 0 C420 120 420 320 490 446 L780 446 L780 0 Z" fill="var(--violet-blue)"/>
      <path d="M560 0 L780 0 L780 118 C690 112 590 150 530 230 C522 130 530 60 560 0 Z" fill="var(--violet-deep)"/>
    </svg>
    <div class="mandala-field" role="img" aria-label="Soft lavender mandala pattern background"
         style="clip-path: path('M0 0 L470 0 C395 120 395 320 465 446 L0 446 Z');"></div>
    <div class="brand-lockup">
      <span class="brand-dot"></span>
      <span class="brand-name">Lotus Path</span>
    </div>
    <div class="contact-name">
      <div class="person">Mara Solene</div>
      <div class="phone">555-014-2287</div>
    </div>
    <div class="contact-web">
      <div>www.lotuspathstudio.com</div>
      <div>hello@lotuspathstudio.com</div>
      <div class="gap">Social: @lotuspathstudio</div>
      <div>Gatherings: lotuspath.events</div>
    </div>
  </section>

  <section class="card card--back" aria-label="Punch card back">
    <div class="wash" role="img" aria-label="Teal to pink watercolour wash"></div>
    <p class="offer">Filling this card<br>with <span class="highlight">9 punches</span><br>gives you $20 off<br>your next visit!</p>
    <div class="punch-grid">
      <span class="punch">$20</span><span class="punch">$20</span><span class="punch">$20</span>
      <span class="punch">$20</span><span class="punch">$20</span><span class="punch">$20</span>
      <span class="punch">$20</span><span class="punch">$20</span><span class="punch">$20</span>
    </div>
    <div class="services-band">
      <p class="services">Tantra – Sexual Healing – Intomacy Coaching<br>Sound Healing – Sound Baths – Crystal Healing – Yoga</p>
      <div class="band-mark">
        <span class="brand-dot"></span>
        <span class="brand-name">Lotus Path</span>
      </div>
    </div>
  </section>

</body>
</html>
```